Brellow Yard Goods needs a spring flyer

We are a local garden centre in Mississauga, Ontario. The product we want to promote is our disposal boxes. These are boxes that can be used to dispose cleanfill, concrete, asphalt, renovation material. Sizes range from 4 yard to 40 yard bins. They can also serve a dual purpose! When customers order a box they can also order any bulk material that we carry to go in the box and essentially get a free delivery. Example: If a customer orders a 4 yard disposal box, they can get up to 4 yards of any material we carry (soils, mulches, gravels) put in the box at the time of delivery. They will only pay the price of the box and the price of the material the delivery is FREE. We would like to see designs that use the colour green. The final design should communicate FREE delivery with box rentals and reliable service! For more information visit our website www.brellowyards-example.com

Target Market(s)

target customer for this flyer is home owners. This will be distributed by mail. Needs to standout amongst all other mail flyers!

Industry/Entity Type

Concrete

Requirements
Must have
• company phone number 905-555-0187

Must have PROMO CODE: QKPLN7390
Nice to have
• a map pin pointing our location 4182 Tundle Lane, Mississauga, Ontario Canada

```html
<!DOCTYPE html>
<html lang="en">
<head>
<meta charset="utf-8">
<title>Brellow Yard Goods – Spring Flyer</title>
<link rel="stylesheet" href="https://fonts.googleapis.com/css2?family=Gelasio:ital,wght@0,400;1,700&family=Arimo:wght@400;700&family=Didact+Gothic&family=Archivo+Narrow:wght@500&display=swap">
<style>
:root{
  --lime:#a2cf2c;
  --lime-light:#b2da3c;
  --ink-green:#1b7a3a;
  --bullet:#1f6f2f;
  --olive:#6e9a1c;
  --red:#a32d17;
  --red-dark:#7e1f0e;
  --cream:#f7e9b0;
  --brown:#6d4a2c;
  --footer-band:#f1ebb0;
  --white:#ffffff;
  --text-dark:#2a2a2a;
  --rule:#8aa84a;
}
*{margin:0;padding:0;box-sizing:border-box}
html,body{width:1200px;height:846px;overflow:hidden;background:var(--white)}
.flyer{position:relative;width:1200px;height:846px;overflow:hidden;
  background:radial-gradient(ellipse at 50% 40%,var(--lime-light),var(--lime) 70%);
  font-family:"Arimo",Arial,sans-serif}
.fold{position:absolute;top:0;width:1px;height:846px;background:var(--rule);opacity:.7}
.heading{position:absolute;font-family:"Gelasio",Georgia,serif;font-weight:400;font-size:54px;color:var(--ink-green);line-height:1}
.list{position:absolute;list-style:none;color:var(--ink-green);font-size:25px;line-height:1}
.list li{position:absolute;left:0;white-space:nowrap;padding-left:19px}
.list li::before{content:"";position:absolute;left:0;top:8px;width:11px;height:11px;border-radius:50%;
  background:radial-gradient(circle at 35% 35%,#5fae4a,var(--bullet) 70%)}
.photo{position:absolute;border:4px solid var(--white);box-shadow:0 1px 3px rgba(0,0,0,.25)}
.ribbon{position:absolute;left:13px;top:542px;width:864px;height:49px}
.ribbon-text{position:absolute;left:158px;top:552px;font-family:"Gelasio",Georgia,serif;font-style:italic;font-weight:700;font-size:22px;color:var(--white);white-space:nowrap;line-height:1.2}
.truck-photo{position:absolute;left:18px;top:591px;width:776px;height:152px}
.free-tag{position:absolute;left:43px;top:534px;width:105px;height:178px}
.free-word{position:absolute;left:43px;top:534px;width:105px;height:160px;display:flex;align-items:center;justify-content:center}
.free-word span{display:block;font-family:"Gelasio",Georgia,serif;font-style:italic;font-weight:700;font-size:46px;color:#2e8a2a;transform:rotate(-90deg);line-height:1;white-space:nowrap}
.order-badge{position:absolute;left:820px;top:323px;width:362px;height:55px}
.order-text{position:absolute;left:820px;top:323px;width:362px;height:55px;display:flex;align-items:center;justify-content:center;font-family:"Gelasio",Georgia,serif;font-style:italic;font-weight:700;font-size:26px;color:var(--cream);letter-spacing:.5px}
.offer-card{position:absolute;left:884px;top:390px;width:302px;height:348px;background:var(--white);box-shadow:0 2px 5px rgba(0,0,0,.3);padding:14px 10px 0 16px;font-family:"Didact Gothic",Arial,sans-serif}
.offer-title{font-size:31px;font-weight:400;color:var(--olive);line-height:1;margin-bottom:10px}
.offer-list{list-style:none;font-size:20px;color:var(--text-dark);line-height:27px}
.offer-list li{display:flex;margin-bottom:3px;white-space:nowrap}
.offer-list .num{color:var(--olive);font-weight:700;width:26px;flex:none}
.footer-band{position:absolute;left:0;top:743px;width:1200px;height:16px;background:var(--footer-band)}
.footer{position:absolute;left:0;top:759px;width:1200px;height:87px;background:var(--white)}
.brand{position:absolute;left:137px;top:780px;display:flex;align-items:center;gap:8px;font-family:"Arimo",Arial,sans-serif;font-weight:700;font-size:17px;color:var(--ink-green);white-space:nowrap}
.brand-mark{width:16px;height:16px;background:var(--ink-green)}
.promo{position:absolute;left:137px;top:808px;font-family:"Arimo",Arial,sans-serif;font-weight:700;font-size:14px;color:var(--red);white-space:nowrap;letter-spacing:.3px}
.phone{position:absolute;left:418px;top:768px;display:flex;align-items:center;gap:8px;font-family:"Archivo Narrow","Arial Narrow",sans-serif;font-weight:500;font-size:57px;color:#111;line-height:1}
.website{position:absolute;left:808px;top:785px;width:392px;text-align:center;font-family:"Arimo",Arial,sans-serif;font-size:24px;color:var(--ink-green);white-space:nowrap}
</style>
</head>
<body>
<main class="flyer">
  <div class="fold" style="left:400px"></div>
  <div class="fold" style="left:800px"></div>

  <!-- Products panel -->
  <h1 class="heading" style="left:30px;top:30px">Products</h1>
  <ul class="list" style="left:48px;top:107px">
    <li style="top:0">Building Supplies</li>
    <li style="top:44px">Concrete/Ready Mix</li>
    <li style="top:87px">Fertilizers</li>
    <li style="top:123px">Mini Disposal Boxes</li>
  </ul>
  <div class="photo" role="img" aria-label="Roll of fresh sod being laid on soil" style="left:17px;top:277px;width:180px;height:120px;background:linear-gradient(160deg,#7fae3f,#6b7a3a 55%,#5a4630)"></div>
  <div class="photo" role="img" aria-label="Green fertilizer spreader on a lawn" style="left:205px;top:277px;width:179px;height:120px;background:linear-gradient(135deg,#9fc45a,#2f6b3a 55%,#cfd6c4)"></div>
  <ul class="list" style="left:48px;top:409px">
    <li style="top:0">Mulch</li>
    <li style="top:35px">Natural Stone</li>
    <li style="top:70px">Sand &amp; Gravel</li>
  </ul>

  <!-- Middle panel -->
  <ul class="list" style="left:430px;top:24px">
    <li style="top:0">Paving Stone</li>
    <li style="top:37px">Paving Stone Product Guide</li>
  </ul>
  <div class="photo" role="img" aria-label="Red mulch bed with a red flower and plants" style="left:414px;top:102px;width:183px;height:121px;background:linear-gradient(135deg,#4e7a32,#7a3424 45%,#2c2623)"></div>
  <div class="photo" role="img" aria-label="Curved paving stone walkway" style="left:604px;top:102px;width:183px;height:121px;background:linear-gradient(135deg,#8a7a6e,#7a675c 50%,#a8a196)"></div>
  <ul class="list" style="left:430px;top:240px">
    <li style="top:0">Sealmarch</li>
    <li style="top:32px">Sod &amp; Grass</li>
  </ul>
  <div class="photo" role="img" aria-label="Stone outdoor fireplace on a patio" style="left:414px;top:306px;width:183px;height:121px;background:linear-gradient(135deg,#a07e5e,#6b3f22 50%,#c48a4a)"></div>
  <div class="photo" role="img" aria-label="Stacked stone wall with floating shelves" style="left:604px;top:306px;width:183px;height:121px;background:linear-gradient(135deg,#e6dac4,#cdbb9c 50%,#efe6d4)"></div>
  <ul class="list" style="left:430px;top:437px">
    <li style="top:0">Soils</li>
    <li style="top:30px">Tierrack Stone</li>
    <li style="top:59px">Winter Products</li>
  </ul>

  <!-- Free delivery band -->
  <svg class="ribbon" viewBox="0 0 864 49" aria-hidden="true">
    <polygon points="0,2 792,2 864,2 830,24.5 864,47 792,47 0,47" fill="var(--red)"/>
    <rect x="0" y="0" width="795" height="3" fill="var(--red-dark)"/>
    <rect x="0" y="46" width="795" height="3" fill="var(--red-dark)"/>
  </svg>
  <div class="ribbon-text">delivery with box rentals ! Pay only for Material &amp; Box!</div>
  <div class="truck-photo" role="img" aria-label="Roll-off truck delivering a blue disposal bin in a parking lot" style="background:linear-gradient(180deg,#8c9186,#a9a69c 40%,#6c6862 75%,#3c3a38)"></div>
  <svg class="free-tag" viewBox="0 0 105 178" aria-hidden="true">
    <polygon points="0,0 105,0 105,178 52.5,158 0,178" fill="var(--cream)"/>
  </svg>
  <div class="free-word"><span>FREE</span></div>

  <!-- Services panel -->
  <h2 class="heading" style="left:840px;top:27px">Services</h2>
  <ul class="list" style="left:886px;top:87px">
    <li style="top:0">Delivery</li>
    <li style="top:32px">Rental Equipment</li>
    <li style="top:63px">Snow Removal</li>
  </ul>
  <div class="photo" role="img" aria-label="Delivery truck loaded with soil in a blue bin" style="left:816px;top:191px;width:179px;height:120px;background:linear-gradient(180deg,#d9dbd6,#8a7060 55%,#6d6a66)"></div>
  <div class="photo" role="img" aria-label="Yellow tracked snow plow clearing snow" style="left:1003px;top:191px;width:180px;height:120px;background:linear-gradient(135deg,#eef0f2,#d8b52c 50%,#c9ced4)"></div>

  <svg class="order-badge" viewBox="0 0 362 55" aria-hidden="true">
    <polygon points="14,0 348,0 362,27.5 348,55 14,55 0,27.5" fill="var(--brown)" stroke="var(--cream)" stroke-width="2"/>
  </svg>
  <div class="order-text">Order a Bin Today !</div>

  <section class="offer-card">
    <h3 class="offer-title">We offer you :</h3>
    <ol class="offer-list">
      <li><span class="num">1.</span><span>Mini Disposal Boxes<br>(Sizes range from 4 yard<br>to 40 yard bins)</span></li>
      <li><span class="num">2.</span><span>Figure out yardage for<br>your Project</span></li>
      <li><span class="num">3.</span><span>Top Soil Specialists</span></li>
      <li><span class="num">4.</span><span>Best Price for Quality<br>Service</span></li>
      <li><span class="num">5.</span><span>Reliable Service</span></li>
      <li><span class="num">6.</span><span>Free Quote</span></li>
    </ol>
  </section>

  <!-- Footer -->
  <div class="footer-band"></div>
  <footer class="footer"></footer>
  <div class="fold" style="left:400px;top:759px;height:87px;background:#b9b9b9"></div>
  <div class="fold" style="left:800px;top:759px;height:87px;background:#b9b9b9"></div>
  <div class="brand"><span class="brand-mark"></span>Brellow Yard Goods</div>
  <div class="promo">PROMO CODE: QKPLN7390</div>
  <div class="phone">
    <svg width="34" height="46" viewBox="0 0 24 32" aria-hidden="true">
      <path d="M6 1 C3 1 1 4 1 9 C1 19 7 29 14 31 C17 32 19 30 20 28 L16 22 C15 21 13 22 12 23 C9 20 7 15 7 11 C8 10 10 9 10 8 L8 1 Z" fill="var(--ink-green)"/>
    </svg>
    905-555-0187
  </div>
  <div class="website">www.brellowyards-example.com</div>
</main>
</body>
</html>
```